Wealth Education Business Needs Sharp Business Card Design

We need a business card design for a recently launched investor education business called Harbor Crest.

The final design should promote security, empowerment, self improvement and financial gain. The card will ideally promote the stature of the business.

For more information and colours please visit harborcrest.com.au

Target Market(s)

Corporate executives and high net worth individuals

Industry/Entity Type

Education

Contact Information for Business Card

Name
Position
Contact Address
Phone
Mobile
Email
Website

```html
<!DOCTYPE html>
<html lang="en">
<head>
<meta charset="utf-8">
<title>Harbor Crest – Business Card</title>
<link href="https://fonts.googleapis.com/css2?family=Lato:wght@400;700&display=swap" rel="stylesheet">
<style>
  :root {
    --backdrop: #2a2a2a;
    --card: #050505;
    --teal: #1597a3;
    --white: #f2f2f2;
    --grey-line: #cfcfcf;
  }
  * { margin: 0; padding: 0; box-sizing: border-box; }
  html, body {
    width: 1200px; height: 873px; overflow: hidden;
    background: var(--backdrop);
    font-family: "Lato", sans-serif;
  }
  .stage {
    position: relative; width: 1200px; height: 873px;
    display: flex; align-items: center; justify-content: center; gap: 40px;
  }
  .card {
    position: relative; width: 540px; height: 310px;
    background: var(--card); border-radius: 18px;
    box-shadow: 0 12px 30px rgba(0,0,0,.45);
    overflow: hidden;
  }
  .brand {
    display: flex; align-items: center; gap: 12px;
    color: var(--white); font-weight: 700; letter-spacing: .18em;
    text-transform: uppercase;
  }
  .brand-dot {
    width: 26px; height: 26px; border-radius: 50%; background: var(--teal);
  }
  .card-front .brand {
    position: absolute; left: 50%; top: 50%; transform: translate(-50%, -50%);
    font-size: 22px;
  }
  .card-back .brand {
    position: absolute; right: 30px; top: 30px; font-size: 16px;
  }
  .card-back .brand-dot { width: 20px; height: 20px; }

  .rule {
    position: absolute; left: 132px; right: 22px; top: 122px; height: 3px;
    background: linear-gradient(to right, var(--grey-line) 0 78%, var(--teal) 78% 100%);
  }
  .person { position: absolute; left: 24px; top: 96px; }
  .person-name { color: var(--white); font-size: 22px; font-weight: 400; line-height: 1; }
  .person-role { color: var(--teal); font-size: 13px; font-weight: 700; letter-spacing: .04em; margin-top: 4px; }

  .contacts { position: absolute; left: 24px; top: 160px; list-style: none; }
  .contacts li {
    display: flex; align-items: center; gap: 10px;
    color: var(--teal); font-size: 14px; font-weight: 700; height: 24px;
  }
  .contacts svg { width: 15px; height: 13px; fill: var(--white); }
  .contacts .web { color: var(--white); margin-top: 4px; }
  .contacts .web span { color: var(--teal); }
  .contacts .white { color: var(--white); }

  .address {
    position: absolute; right: 26px; top: 160px;
    color: var(--teal); font-size: 13px; font-weight: 700; line-height: 1.45;
  }
  .address .white { color: var(--white); }
</style>
</head>
<body>
<main class="stage">
  <section class="card card-front" aria-label="Card front">
    <div class="brand"><span class="brand-dot"></span>Harbor Crest</div>
  </section>

  <section class="card card-back" aria-label="Card back">
    <div class="brand"><span class="brand-dot"></span>Harbor Crest</div>
    <div class="rule"></div>
    <div class="person">
      <p class="person-name">Daniel Reeves</p>
      <p class="person-role">DIRECTOR</p>
    </div>
    <ul class="contacts">
      <li>
        <svg viewBox="0 0 16 14" aria-hidden="true"><path d="M1 4c0-2 3-3 7-3s7 1 7 3v1h-4V4H5v1H1zM3 6h10l2 7H1z"/></svg>
        0049 170 2281904
      </li>
      <li>
        <svg viewBox="0 0 16 14" aria-hidden="true"><path d="M4 0h8v4H4zM1 5h14v6h-3v3H4v-3H1zM5 9v4h6V9z"/></svg>
        0049 170 2281905
      </li>
      <li>
        <svg viewBox="0 0 16 14" aria-hidden="true"><path d="M0 1h16v12H0zM1.5 2.5v.6L8 8l6.5-4.9v-.6zM1.5 5v6.5h13V5L8 10z"/></svg>
        info@harborcrest<span class="white">.com.au</span>
      </li>
      <li class="web">www.<span>harborcrest</span>.com.au</li>
    </ul>
    <p class="address">2280 Harbour View Road,<br>Seabrook Point, <span class="white">Florida 33190</span></p>
  </section>
</main>
</body>
</html>
```